Update Powerpoint Presentation

We need to update the existing Powerpoint presentation to make it look more professional, less words and get the message across to potential clients. Our clients are banks and lenders in Australia.
Reason: To give the designers more time to come up with designs
Reason: I am looking for a design that is more innovative and doesn't just re-create what I gave. This presentation is only an example of what I would like I am keen to find a presentation that takes it to the next level.

```html
<!DOCTYPE html>
<html lang="en">
<head>
<meta charset="utf-8">
<title>Kestrel – Company Presentation Slides</title>
<link href="https://fonts.googleapis.com/css2?family=Open+Sans:wght@400;600;700;800&display=swap" rel="stylesheet">
<style>
:root{
  --page:#1c1c1e;
  --navy:#1a3d78;
  --blue:#2a63b0;
  --sky:#4d8fd6;
  --light:#9cc0e8;
  --pale:#dce7f4;
  --ink:#2d3544;
  --grey:#7c8594;
  --white:#ffffff;
}
*{box-sizing:border-box;margin:0;padding:0}
html,body{width:1200px;height:3261px;overflow:hidden;background:var(--page)}
body{font-family:'Open Sans',Arial,sans-serif;color:var(--ink)}
.sheet{width:1200px;height:3261px;padding:21px 30px;display:grid;grid-template-columns:556px 556px;grid-template-rows:repeat(8,384px);column-gap:28px;row-gap:21px}
.slide{position:relative;overflow:hidden;background:linear-gradient(180deg,#ffffff 0%,#f1f3f6 70%,#e6e9ee 100%)}
.abs{position:absolute}
.title-mark{position:absolute;left:0;top:18px;width:26px;height:26px;background:var(--navy)}
.slide-title{position:absolute;left:40px;top:15px;width:480px;font-weight:700;font-size:19px;line-height:1.17;color:var(--navy);text-transform:uppercase}
.footer{position:absolute;left:0;bottom:0;width:556px;height:72px}
.footer-logo{position:absolute;left:0;right:0;bottom:14px;text-align:center;color:var(--white);font-weight:800;font-size:17px;letter-spacing:1px}
.body-text{font-size:7.5px;line-height:1.5;color:var(--grey)}
.body-text p+p{margin-top:8px}
.photo{background:linear-gradient(160deg,#b9cde4 0%,#6f8fb5 55%,#3d5a86 100%)}
.portrait{background:linear-gradient(170deg,#e9dccd 0%,#c4a892 60%,#8a7666 100%)}
.round{border-radius:50%}
.item-head{font-size:8px;font-weight:700;color:var(--navy)}
.item-text{font-size:7px;line-height:1.45;color:var(--grey)}
.num{width:30px;height:30px;border-radius:50%;background:var(--blue);color:var(--white);font-weight:700;font-size:13px;display:flex;align-items:center;justify-content:center}
.logo-big{font-weight:800;color:var(--navy);letter-spacing:2px;text-align:center}
.info-box{background:var(--sky);color:var(--white);font-size:7.5px;line-height:1.5;padding:12px}
.center-row{display:flex;justify-content:center}
.bullet-circle{width:92px;height:92px;border-radius:50%;background:rgba(77,143,214,.55);border:2px solid var(--white);margin-left:-14px;display:flex;align-items:center;justify-content:center;color:var(--white);font-size:9px;font-weight:700}
.bullet-circle:first-child{margin-left:0}
.person{display:flex;gap:8px;align-items:flex-start}
.legend{font-size:6.5px;color:var(--grey);display:flex;gap:8px}
.legend i{display:inline-block;width:7px;height:7px;margin-right:3px;vertical-align:middle}
</style>
</head>
<body>
<main class="sheet">

<!-- 1 Cover -->
<section class="slide">
  <div class="abs logo-big" style="left:0;right:0;top:28px;font-size:36px">KESTREL</div>
  <div class="abs body-text" style="left:0;right:0;top:92px;text-align:center">Prepared for banks and lenders</div>
  <div class="abs" style="left:0;right:0;top:104px;text-align:center;font-weight:800;font-size:22px;color:var(--navy)">COMPANY PRESENTATION</div>
  <div class="abs portrait" role="img" aria-label="Presenter portrait photo" style="left:250px;top:148px;width:56px;height:68px"></div>
  <div class="abs body-text" style="left:0;right:0;top:222px;text-align:center;line-height:1.4">
    <div style="font-weight:700;color:var(--navy)">Presenter Name</div>
    <div>Managing Director</div>
    <div>Sydney Office, Level 12</div>
  </div>
  <svg class="abs" style="left:0;bottom:0" width="556" height="110" viewBox="0 0 556 110">
    <path d="M0 40 C160 5 380 10 556 45 L556 110 L0 110Z" fill="var(--light)"/>
    <path d="M0 52 C170 20 380 24 556 58 L556 110 L0 110Z" fill="var(--navy)"/>
  </svg>
</section>

<!-- 2 Photo + text -->
<section class="slide">
  <div class="title-mark"></div>
  <h2 class="slide-title">Slide presentation Harlow Capital<br>powerful mission 1</h2>
  <div class="abs photo" role="img" aria-label="Photo of a city office tower" style="left:40px;top:74px;width:150px;height:200px"></div>
  <div class="abs body-text" style="left:210px;top:78px;width:310px">
    <p>Our team brings a clear, steady approach to lending research, helping banks and lenders see what matters and act with confidence.</p>
    <p>Our team brings a clear, steady approach to lending research, helping banks and lenders see what matters and act with confidence.</p>
  </div>
  <svg class="footer" viewBox="0 0 556 72"><path d="M0 24 C170 2 390 4 556 26 L556 72 L0 72Z" fill="var(--light)"/><path d="M0 34 C170 12 390 14 556 36 L556 72 L0 72Z" fill="var(--navy)"/></svg>
  <div class="footer-logo">KESTREL</div>
</section>

<!-- 3 Numbered list -->
<section class="slide">
  <div class="title-mark"></div>
  <h2 class="slide-title">Slide presentation Harlow Capital<br>powerful mission 1</h2>
  <div class="abs" style="left:40px;top:80px;width:470px;display:grid;row-gap:18px">
    <div class="person"><div class="num">1</div><div><div class="item-head">We know lending</div><div class="item-text">Practical insight for Australian lenders, shared in a plain and useful way.</div></div></div>
    <div class="person"><div class="num">2</div><div><div class="item-head">We know lending</div><div class="item-text">Practical insight for Australian lenders, shared in a plain and useful way.</div></div></div>
    <div class="person"><div class="num">3</div><div><div class="item-head">We know lending</div><div class="item-text">Practical insight for Australian lenders, shared in a plain and useful way.</div></div></div>
    <div class="person"><div class="num">4</div><div><div class="item-head">We know lending</div><div class="item-text">Practical insight for Australian lenders, shared in a plain and useful way.</div></div></div>
  </div>
  <svg class="footer" viewBox="0 0 556 72"><path d="M0 24 C170 2 390 4 556 26 L556 72 L0 72Z" fill="var(--light)"/><path d="M0 34 C170 12 390 14 556 36 L556 72 L0 72Z" fill="var(--navy)"/></svg>
  <div class="footer-logo">KESTREL</div>
</section>

<!-- 4 People list -->
<section class="slide">
  <div class="title-mark"></div>
  <h2 class="slide-title">Slide presentation Harlow Capital<br>powerful mission 1</h2>
  <div class="abs" style="left:40px;top:78px;width:470px;display:grid;row-gap:14px">
    <div class="person"><div class="portrait round" role="img" aria-label="Team member portrait" style="width:34px;height:34px;flex:none"></div><div><div class="item-head">We know lending</div><div class="item-text">Practical insight for Australian lenders, shared in a plain and useful way.</div></div></div>
    <div class="person"><div class="portrait round" role="img" aria-label="Team member portrait" style="width:34px;height:34px;flex:none"></div><div><div class="item-head">We know lending</div><div class="item-text">Practical insight for Australian lenders, shared in a plain and useful way.</div></div></div>
    <div class="person"><div class="portrait round" role="img" aria-label="Team member portrait" style="width:34px;height:34px;flex:none"></div><div><div class="item-head">We know lending</div><div class="item-text">Practical insight for Australian lenders, shared in a plain and useful way.</div></div></div>
    <div class="person"><div class="portrait round" role="img" aria-label="Team member portrait" style="width:34px;height:34px;flex:none"></div><div><div class="item-head">We know lending</div><div class="item-text">Practical insight for Australian lenders, shared in a plain and useful way.</div></div></div>
  </div>
  <svg class="footer" viewBox="0 0 556 72"><path d="M0 24 C170 2 390 4 556 26 L556 72 L0 72Z" fill="var(--light)"/><path d="M0 34 C170 12 390 14 556 36 L556 72 L0 72Z" fill="var(--navy)"/></svg>
  <div class="footer-logo">KESTREL</div>
</section>

<!-- 5 Cycle diagram -->
<section class="slide">
  <div class="title-mark"></div>
  <h2 class="slide-title">Slide presentation Harlow Capital<br>powerful mission 1</h2>
  <div class="abs body-text" style="left:40px;top:78px;width:200px">
    <p>Our team brings a clear, steady approach to lending research, helping banks and lenders see what matters and act with confidence.</p>
    <p>Our team brings a clear, steady approach to lending research, helping banks and lenders see what matters and act with confidence.</p>
  </div>
  <svg class="abs" style="left:270px;top:70px" width="250" height="230" viewBox="0 0 250 230" font-family="Open Sans, sans-serif" font-size="8" text-anchor="middle">
    <g stroke="var(--light)" stroke-width="2">
      <line x1="125" y1="115" x2="125" y2="30"/><line x1="125" y1="115" x2="200" y2="72"/><line x1="125" y1="115" x2="200" y2="158"/>
      <line x1="125" y1="115" x2="125" y2="200"/><line x1="125" y1="115" x2="50" y2="158"/><line x1="125" y1="115" x2="50" y2="72"/>
    </g>
    <circle cx="125" cy="115" r="34" fill="var(--navy)"/><text x="125" y="118" fill="#fff" font-weight="700" font-size="9">Process</text>
    <g fill="var(--sky)">
      <circle cx="125" cy="30" r="25"/><circle cx="200" cy="72" r="25"/><circle cx="200" cy="158" r="25"/>
      <circle cx="125" cy="200" r="25"/><circle cx="50" cy="158" r="25"/><circle cx="50" cy="72" r="25"/>
    </g>
    <g fill="#fff" font-weight="600">
      <text x="125" y="33">Research</text><text x="200" y="75">Review</text><text x="200" y="161">Report</text>
      <text x="125" y="203">Advise</text><text x="50" y="161">Lend</text><text x="50" y="75">Grow</text>
    </g>
  </svg>
  <svg class="footer" viewBox="0 0 556 72"><path d="M0 24 C170 2 390 4 556 26 L556 72 L0 72Z" fill="var(--light)"/><path d="M0 34 C170 12 390 14 556 36 L556 72 L0 72Z" fill="var(--navy)"/></svg>
  <div class="footer-logo">KESTREL</div>
</section>

<!-- 6 Three main point -->
<section class="slide">
  <div class="title-mark"></div>
  <h2 class="slide-title">Three main point</h2>
  <div class="abs" style="left:40px;top:62px;width:480px;display:grid;grid-template-columns:repeat(3,1fr);column-gap:20px">
    <div><div class="portrait" role="img" aria-label="Portrait photo" style="height:120px"></div><p class="item-text" style="margin-top:8px">Practical insight for Australian lenders, shared in a plain and useful way.</p></div>
    <div><div class="portrait" role="img" aria-label="Portrait photo" style="height:120px"></div><p class="item-text" style="margin-top:8px">Practical insight for Australian lenders, shared in a plain and useful way.</p></div>
    <div><div class="portrait" role="img" aria-label="Portrait photo" style="height:120px"></div><p class="item-text" style="margin-top:8px">Practical insight for Australian lenders, shared in a plain and useful way.</p></div>
  </div>
  <svg class="footer" viewBox="0 0 556 72"><path d="M0 24 C170 2 390 4 556 26 L556 72 L0 72Z" fill="var(--light)"/><path d="M0 34 C170 12 390 14 556 36 L556 72 L0 72Z" fill="var(--navy)"/></svg>
  <div class="footer-logo">KESTREL</div>
</section>

<!-- 7 World map -->
<section class="slide">
  <div class="title-mark"></div>
  <h2 class="slide-title">Slide presentation Harlow Capital<br>powerful mission 1</h2>
  <div class="abs" role="img" aria-label="World map showing office regions" style="left:40px;top:82px;width:300px;height:160px;background:linear-gradient(135deg,#7fb0e4,#3a73bd);border-radius:40px 80px 60px 30px"></div>
  <div class="abs body-text" style="left:40px;top:252px">Offices across five regions</div>
  <svg class="footer" viewBox="0 0 556 72"><path d="M0 24 C170 2 390 4 556 26 L556 72 L0 72Z" fill="var(--light)"/><path d="M0 34 C170 12 390 14 556 36 L556 72 L0 72Z" fill="var(--navy)"/></svg>
  <div class="footer-logo">KESTREL</div>
</section>

<!-- 8 Divider -->
<section class="slide">
  <svg class="abs" style="left:0;top:0" width="556" height="384" viewBox="0 0 556 384">
    <path d="M0 140 C180 100 380 110 556 160 L556 330 C380 300 180 320 0 350Z" fill="var(--light)"/>
    <path d="M0 152 C180 114 380 122 556 172 L556 320 C380 292 180 310 0 340Z" fill="var(--navy)"/>
    <path d="M0 190 C200 160 380 170 556 210" stroke="var(--blue)" stroke-width="18" fill="none" opacity=".6"/>
  </svg>
  <div class="abs" style="left:50px;top:178px;color:#fff;font-weight:800;font-size:28px;letter-spacing:2px">KESTREL</div>
  <div class="abs" style="left:50px;top:222px;color:#fff;font-weight:800;font-size:22px">DIVIDER PAGES HERE</div>
  <div class="abs" style="left:50px;top:256px;color:var(--pale);font-size:7px">Sydney, April 2024</div>
  <div class="abs" style="right:30px;top:262px;color:#fff;font-weight:700;font-size:9px">COMPANY PRESENTATION</div>
</section>

<!-- 9 Bullet circles -->
<section class="slide">
  <div class="title-mark"></div>
  <h2 class="slide-title">Slide presentation Harlow Capital<br>page with bulletpoint 1</h2>
  <div class="abs center-row" style="left:40px;top:76px;width:330px;justify-content:flex-start">
    <div class="bullet-circle" style="background:rgba(156,192,232,.8)">PLAN</div>
    <div class="bullet-circle" style="background:rgba(77,143,214,.75)">BUILD</div>
    <div class="bullet-circle" style="background:rgba(42,99,176,.8)">REVIEW</div>
    <div class="bullet-circle" style="background:rgba(26,61,120,.85)">DELIVER</div>
  </div>
  <div class="abs body-text" style="left:40px;top:190px;width:470px">
    <p>Our team brings a clear, steady approach to lending research, helping banks and lenders see what matters and act with confidence.</p>
    <p>Our team brings a clear, steady approach to lending research, helping banks and lenders see what matters and act with confidence.</p>
  </div>
  <svg class="footer" viewBox="0 0 556 72"><path d="M0 24 C170 2 390 4 556 26 L556 72 L0 72Z" fill="var(--light)"/><path d="M0 34 C170 12 390 14 556 36 L556 72 L0 72Z" fill="var(--navy)"/></svg>
  <div class="footer-logo">KESTREL</div>
</section>

<!-- 10 Nested layers -->
<section class="slide">
  <div class="title-mark"></div>
  <h2 class="slide-title">Slide presentation Harlow Capital<br>page with bulletpoint 1</h2>
  <div class="abs body-text" style="left:40px;top:80px;width:230px">
    <p>Our team brings a clear, steady approach to lending research, helping banks and lenders see what matters and act with confidence.</p>
    <p>Our team brings a clear, steady approach to lending research, helping banks and lenders see what matters and act with confidence.</p>
  </div>
  <svg class="abs" style="left:320px;top:72px" width="180" height="230" viewBox="0 0 180 230">
    <ellipse cx="90" cy="130" rx="88" ry="98" fill="var(--pale)"/>
    <ellipse cx="90" cy="146" rx="72" ry="80" fill="var(--light)"/>
    <ellipse cx="90" cy="162" rx="56" ry="62" fill="var(--sky)"/>
    <ellipse cx="90" cy="178" rx="40" ry="44" fill="var(--blue)"/>
    <ellipse cx="90" cy="194" rx="24" ry="26" fill="var(--navy)"/>
  </svg>
  <svg class="footer" viewBox="0 0 556 72"><path d="M0 24 C170 2 390 4 556 26 L556 72 L0 72Z" fill="var(--light)"/><path d="M0 34 C170 12 390 14 556 36 L556 72 L0 72Z" fill="var(--navy)"/></svg>
  <div class="footer-logo">KESTREL</div>
</section>

<!-- 11 Photo + info box -->
<section class="slide">
  <div class="title-mark"></div>
  <h2 class="slide-title">Slide presentation Harlow Capital<br>powerful mission 1</h2>
  <div class="abs photo" role="img" aria-label="Photo of city buildings" style="left:40px;top:76px;width:210px;height:100px"></div>
  <div class="abs body-text" style="left:40px;top:186px;width:300px">
    <p>Our team brings a clear, steady approach to lending research, helping banks and lenders see what matters and act with confidence.</p>
    <p>Our team brings a clear, steady approach to lending research, helping banks and lenders see what matters and act with confidence.</p>
  </div>
  <div class="abs info-box" style="left:372px;top:70px;width:150px;height:200px">Our team brings a clear, steady approach to lending research, helping banks and lenders see what matters and act with confidence.</div>
  <svg class="footer" viewBox="0 0 556 72"><path d="M0 24 C170 2 390 4 556 26 L556 72 L0 72Z" fill="var(--light)"/><path d="M0 34 C170 12 390 14 556 36 L556 72 L0 72Z" fill="var(--navy)"/></svg>
  <div class="footer-logo">KESTREL</div>
</section>

<!-- 12 Pie chart -->
<section class="slide">
  <div class="title-mark"></div>
  <h2 class="slide-title">Slide presentation Harlow Capital<br>powerful mission 1</h2>
  <div class="abs body-text" style="left:40px;top:80px;width:220px">
    <p>Our team brings a clear, steady approach to lending research, helping banks and lenders see what matters and act with confidence.</p>
    <p>Our team brings a clear, steady approach to lending research, helping banks and lenders see what matters and act with confidence.</p>
  </div>
  <svg class="abs" style="left:320px;top:80px" width="160" height="160" viewBox="0 0 160 160">
    <g transform="rotate(-90 80 80)" fill="none" stroke-width="70">
      <circle cx="80" cy="80" r="35" stroke="var(--navy)" stroke-dasharray="98.9 220"/>
      <circle cx="80" cy="80" r="35" stroke="var(--blue)" stroke-dasharray="55 220" stroke-dashoffset="-98.9"/>
      <circle cx="80" cy="80" r="35" stroke="var(--sky)" stroke-dasharray="39.6 220" stroke-dashoffset="-153.9"/>
      <circle cx="80" cy="80" r="35" stroke="var(--light)" stroke-dasharray="26.4 220" stroke-dashoffset="-193.5"/>
    </g>
  </svg>
  <div class="abs legend" style="left:300px;top:252px">
    <span><i style="background:var(--navy)"></i>Banks</span><span><i style="background:var(--blue)"></i>Lenders</span><span><i style="background:var(--sky)"></i>Brokers</span><span><i style="background:var(--light)"></i>Other</span>
  </div>
  <svg class="footer" viewBox="0 0 556 72"><path d="M0 24 C170 2 390 4 556 26 L556 72 L0 72Z" fill="var(--light)"/><path d="M0 34 C170 12 390 14 556 36 L556 72 L0 72Z" fill="var(--navy)"/></svg>
  <div class="footer-logo">KESTREL</div>
</section>

<!-- 13 Bar chart -->
<section class="slide">
  <div class="title-mark"></div>
  <h2 class="slide-title">Slide presentation Harlow Capital<br>powerful mission 1</h2>
  <div class="abs body-text" style="left:40px;top:80px;width:210px">
    <p>Our team brings a clear, steady approach to lending research, helping banks and lenders see what matters and act with confidence.</p>
    <p>Our team brings a clear, steady approach to lending research, helping banks and lenders see what matters and act with confidence.</p>
  </div>
  <svg class="abs" style="left:290px;top:100px" width="230" height="180" viewBox="0 0 230 180" font-family="Open Sans, sans-serif" font-size="7" fill="var(--grey)" text-anchor="middle">
    <g>
      <path d="M20 150 h34 v-50 h-34z" fill="var(--sky)"/><path d="M20 100 l10 -8 h34 l-10 8z" fill="var(--light)"/><path d="M54 150 l10 -8 v-50 l-10 8z" fill="var(--blue)"/>
      <path d="M70 150 h34 v-75 h-34z" fill="var(--sky)"/><path d="M70 75 l10 -8 h34 l-10 8z" fill="var(--light)"/><path d="M104 150 l10 -8 v-75 l-10 8z" fill="var(--blue)"/>
      <path d="M120 150 h34 v-100 h-34z" fill="var(--sky)"/><path d="M120 50 l10 -8 h34 l-10 8z" fill="var(--light)"/><path d="M154 150 l10 -8 v-100 l-10 8z" fill="var(--blue)"/>
      <path d="M170 150 h34 v-125 h-34z" fill="var(--blue)"/><path d="M170 25 l10 -8 h34 l-10 8z" fill="var(--sky)"/><path d="M204 150 l10 -8 v-125 l-10 8z" fill="var(--navy)"/>
    </g>
    <text x="37" y="166">2021</text><text x="87" y="166">2022</text><text x="137" y="166">2023</text><text x="187" y="166">2024</text>
  </svg>
  <svg class="footer" viewBox="0 0 556 72"><path d="M0 24 C170 2 390 4 556 26 L556 72 L0 72Z" fill="var(--light)"/><path d="M0 34 C170 12 390 14 556 36 L556 72 L0 72Z" fill="var(--navy)"/></svg>
  <div class="footer-logo">KESTREL</div>
</section>

<!-- 14 Text + team -->
<section class="slide">
  <div class="title-mark"></div>
  <h2 class="slide-title">Slide presentation Harlow Capital<br>powerful mission 1</h2>
  <div class="abs body-text" style="left:40px;top:80px;width:280px">
    <p>Our team brings a clear, steady approach to lending research, helping banks and lenders see what matters and act with confidence.</p>
    <p>Our team brings a clear, steady approach to lending research, helping banks and lenders see what matters and act with confidence.</p>
  </div>
  <div class="abs" style="left:370px;top:76px;display:grid;row-gap:12px">
    <div class="person"><div class="portrait round" role="img" aria-label="Team member portrait" style="width:34px;height:34px"></div><div><div class="item-head">Client Name</div><div class="item-text">Role title here</div></div></div>
    <div class="person"><div class="portrait round" role="img" aria-label="Team member portrait" style="width:34px;height:34px"></div><div><div class="item-head">Client Name</div><div class="item-text">Role title here</div></div></div>
    <div class="person"><div class="portrait round" role="img" aria-label="Team member portrait" style="width:34px;height:34px"></div><div><div class="item-head">Client Name</div><div class="item-text">Role title here</div></div></div>
    <div class="person"><div class="portrait round" role="img" aria-label="Team member portrait" style="width:34px;height:34px"></div><div><div class="item-head">Client Name</div><div class="item-text">Role title here</div></div></div>
  </div>
  <svg class="footer" viewBox="0 0 556 72"><path d="M0 24 C170 2 390 4 556 26 L556 72 L0 72Z" fill="var(--light)"/><path d="M0 34 C170 12 390 14 556 36 L556 72 L0 72Z" fill="var(--navy)"/></svg>
  <div class="footer-logo">KESTREL</div>
</section>

<!-- 15 Testimonials -->
<section class="slide">
  <div class="title-mark"></div>
  <h2 class="slide-title">Testimonial client 2</h2>
  <div class="abs" style="left:40px;top:62px;width:480px;display:grid;grid-template-columns:1fr 1fr;gap:20px 24px">
    <div class="person"><div class="portrait round" role="img" aria-label="Client portrait" style="width:34px;height:34px;flex:none"></div><div><div class="item-head">Client Name</div><div class="item-head" style="color:var(--sky)">Company Ltd</div><div class="item-text">Clear advice and steady support from start to finish. We would gladly work with this team again.</div></div></div>
    <div class="person"><div class="portrait round" role="img" aria-label="Client portrait" style="width:34px;height:34px;flex:none"></div><div><div class="item-head">Client Name</div><div class="item-head" style="color:var(--sky)">Company Ltd</div><div class="item-text">Clear advice and steady support from start to finish. We would gladly work with this team again.</div></div></div>
    <div class="person"><div class="portrait round" role="img" aria-label="Client portrait" style="width:34px;height:34px;flex:none"></div><div><div class="item-head">Client Name</div><div class="item-head" style="color:var(--sky)">Company Ltd</div><div class="item-text">Clear advice and steady support from start to finish. We would gladly work with this team again.</div></div></div>
    <div class="person"><div class="portrait round" role="img" aria-label="Client portrait" style="width:34px;height:34px;flex:none"></div><div><div class="item-head">Client Name</div><div class="item-head" style="color:var(--sky)">Company Ltd</div><div class="item-text">Clear advice and steady support from start to finish. We would gladly work with this team again.</div></div></div>
  </div>
  <svg class="footer" viewBox="0 0 556 72"><path d="M0 24 C170 2 390 4 556 26 L556 72 L0 72Z" fill="var(--light)"/><path d="M0 34 C170 12 390 14 556 36 L556 72 L0 72Z" fill="var(--navy)"/></svg>
  <div class="footer-logo">KESTREL</div>
</section>

<!-- 16 Thank you -->
<section class="slide">
  <div class="abs logo-big" style="left:0;right:0;top:90px;font-size:40px">KESTREL</div>
  <svg class="abs" style="left:0;bottom:0" width="556" height="150" viewBox="0 0 556 150">
    <path d="M0 40 C180 0 380 6 556 36 L556 150 L0 150Z" fill="var(--light)"/>
    <path d="M0 54 C180 16 380 20 556 50 L556 150 L0 150Z" fill="var(--navy)"/>
  </svg>
  <div class="abs" style="left:40px;top:300px;color:#fff;font-weight:800;font-size:26px">THANK YOU</div>
  <div class="abs" style="left:40px;top:340px;color:var(--pale);font-size:7px">Sydney, April 2024</div>
  <div class="abs" style="right:30px;top:312px;color:#fff;font-weight:700;font-size:9px">COMPANY PRESENTATION</div>
</section>

</main>
</body>
</html>
```